Brenner Business Cards

Front of business card will have logo, name, address, & telephone number. Back of card will have a list of services provided - Roads, Substation Pads, Temporary Pads, Site Pads, Land Leveling, Powerline Row Cleaning, Land Clearing, Gates, Fencing, Construction Entrances, Excavation, Trenching, Underground Utilities, Directional Boring, Pile Driving. We are a construction company that uses heavy equipment like bulldozers, motor graders/blades, dump trucks, backhoes, hydro axes, & skid loaders. We build roads, pads, & install electric utility lines & waterlines underground. This logo is new. The word "Construction" can be smaller as uploaded 2 example edited logos. We will be using this card design for many employees.
Target Market(s)
Industrial Electric Powerline, Wind Turbine, Solar Panel, & Water Utility companies.
Contact Information for Business Card
Name/Position - Danny Brenner - Owner
Address: 4837 FM 952
Ridgeway, OK 79284
Phone number - (555) 518-2906

```html
<!DOCTYPE html>
<html lang="en">
<head>
<meta charset="utf-8">
<title>Brenner Construction Business Cards</title>
<link rel="stylesheet" href="https://fonts.googleapis.com/css2?family=Arimo:wght@400;700&display=swap">
<style>
  :root {
    --maroon: #3a111b;
    --paper: #ffffff;
    --backdrop: #8c8c8c;
    --ink-light: #f4eef0;
    --ink-dark: #151515;
    --rule: #7a4a55;
  }
  * { margin: 0; padding: 0; box-sizing: border-box; }
  html, body {
    width: 1200px; height: 1200px; overflow: hidden;
    background: var(--backdrop);
    font-family: "Arimo", Arial, sans-serif;
  }
  .stage { position: relative; width: 1200px; height: 1200px; }
  .card { position: absolute; top: 310px; height: 594px; }
  .card-front { left: 234px; width: 364px; background: var(--paper); color: var(--maroon); }
  .card-back { left: 627px; width: 370px; background: var(--maroon); color: var(--ink-light); }

  .brand {
    position: absolute; top: 118px; left: 0; right: 0;
    display: flex; flex-direction: column; align-items: center; gap: 14px;
  }
  .brand-mark { width: 22px; height: 22px; border-radius: 50%; background: var(--maroon); }
  .brand-name {
    font-size: 30px; font-weight: 700; line-height: 1.25;
    text-transform: uppercase; text-align: center; letter-spacing: 1px;
  }
  .person { position: absolute; top: 354px; left: 0; right: 0; text-align: center; }
  .person-name { font-size: 29px; font-weight: 700; letter-spacing: 0.5px; line-height: 32px; }
  .person-title { font-size: 20px; line-height: 24px; margin-top: 2px; }
  .phone-band {
    position: absolute; top: 424px; left: 0; right: 0; height: 62px;
    background: var(--maroon); color: var(--paper);
    display: flex; align-items: center; justify-content: center;
    font-size: 24px; font-weight: 700;
  }
  .address {
    position: absolute; top: 500px; left: 0; right: 0;
    text-align: center; font-size: 21px; line-height: 26px; color: var(--ink-dark);
  }

  .back-content { padding-top: 85px; text-align: center; font-size: 16.5px; line-height: 22.4px; }
  .divider { width: 148px; height: 1px; background: var(--rule); margin: 21px auto 24px; }
</style>
</head>
<body>
<main class="stage">
  <section class="card card-front">
    <div class="brand">
      <span class="brand-mark"></span>
      <span class="brand-name">Brenner<br>Construction</span>
    </div>
    <div class="person">
      <div class="person-name">DANNY BRENNER</div>
      <div class="person-title">Owner</div>
    </div>
    <div class="phone-band">(555) 518-2906</div>
    <div class="address">4837 FM 952<br>Ridgeway, OK 79284</div>
  </section>

  <section class="card card-back">
    <div class="back-content">
      <p class="services">Roads, Substation Pads<br>Temporary Pads<br>Site Pads, | Land Leveling | Powerline<br>Row Cleaning | Land Clearing<br>Gates | Fencing,Construction Entrances<br>Excavation | Trenching<br>Underground Utilities<br>Directional Boring | Pile Driving.</p>
      <div class="divider"></div>
      <p class="equipment">We are a construction company that<br>uses heavy equipment<br>like bulldozers | motor graders/blades<br>dump trucks<br>backhoes | hydro axes &amp; skid loaders.</p>
      <div class="divider"></div>
      <p class="mission">We build roads, pads<br>install electric utility lines<br>waterlines underground.</p>
    </div>
  </section>
</main>
</body>
</html>
```